Looking for awesome business card design with attached existing logo

We are a water, mold, and fire damage restoration company called "Solvane Crest" Looking for an awesome business card that is edgy yet professional and unique. Show me what you got!

```html
<!DOCTYPE html>
<html lang="en">
<head>
<meta charset="utf-8">
<title>Solvane Crest — Business Card</title>
<link href="https://fonts.googleapis.com/css2?family=Montserrat:wght@400;500;600;700;800&display=swap" rel="stylesheet">
<style>
  :root {
    --teal: #2c4856;
    --gold: #d89b2b;
    --red: #b3162b;
    --grey: #7d7d7d;
    --white: #ffffff;
    --stage: #3a3a3b;
  }
  * { box-sizing: border-box; margin: 0; padding: 0; }
  html, body { width: 1200px; height: 987px; overflow: hidden; }
  body {
    background: var(--stage);
    font-family: "Montserrat", sans-serif;
    position: relative;
  }
  .card {
    position: absolute;
    width: 560px;
    height: 320px;
    box-shadow: 0 14px 34px rgba(0,0,0,0.45);
  }
  .card-front {
    left: 150px; top: 110px;
    background: var(--teal);
    display: flex; align-items: center; justify-content: center;
  }
  .card-back {
    left: 490px; top: 540px;
    background: var(--white);
    display: flex; align-items: center;
  }
  .brand {
    display: flex; align-items: center; gap: 12px;
    font-weight: 800;
    font-size: 38px;
    letter-spacing: 1px;
    text-transform: uppercase;
  }
  .brand-dot {
    width: 18px; height: 18px; border-radius: 50%;
    background: var(--gold);
  }
  .card-front .brand-name { color: var(--white); }
  .card-back .brand { font-size: 29px; gap: 9px; }
  .card-back .brand-dot { width: 14px; height: 14px; }
  .card-back .brand-name { color: var(--teal); }
  .back-brand-area {
    width: 280px; display: flex; justify-content: center;
  }
  .divider {
    width: 2px; height: 165px; background: var(--teal);
  }
  .contact-block { padding-left: 30px; }
  .person-name { color: var(--teal); font-weight: 700; font-size: 22px; line-height: 1.1; }
  .person-role { color: var(--red); font-weight: 500; font-size: 14px; margin-bottom: 14px; }
  .address { color: var(--grey); font-size: 13px; line-height: 1.4; margin-bottom: 14px; padding-left: 14px; }
  .contact-list { list-style: none; padding-left: 22px; }
  .contact-list li {
    display: flex; align-items: center; gap: 8px;
    color: var(--grey); font-size: 14px; line-height: 1.45;
  }
  .contact-list svg { width: 13px; height: 13px; flex: none; }
</style>
</head>
<body>
  <section class="card card-front" aria-label="Card front">
    <div class="brand">
      <span class="brand-dot"></span>
      <span class="brand-name">Solvane Crest</span>
    </div>
  </section>

  <section class="card card-back" aria-label="Card back">
    <div class="back-brand-area">
      <div class="brand">
        <span class="brand-dot"></span>
        <span class="brand-name">Solvane Crest</span>
      </div>
    </div>
    <div class="divider"></div>
    <div class="contact-block">
      <p class="person-name">Marcus Hale</p>
      <p class="person-role">President</p>
      <p class="address">Street Name Ave, Suite 25<br>State, Zip Code, Country</p>
      <ul class="contact-list">
        <li>
          <svg viewBox="0 0 16 16" aria-hidden="true"><path fill="#d89b2b" d="M3.5 1l2.5 3-1.5 2c1 2 3 4 5 5l2-1.5 3 2.5-1.5 2.5C7 15 1 9 1 2.5z"/></svg>
          012-555-0142
        </li>
        <li>
          <svg viewBox="0 0 16 16" aria-hidden="true"><rect x="4" y="1" width="8" height="14" rx="1.5" fill="none" stroke="#d89b2b" stroke-width="1.6"/><circle cx="8" cy="12.5" r="0.9" fill="#d89b2b"/></svg>
          012-555-0187
        </li>
        <li>
          <svg viewBox="0 0 16 16" aria-hidden="true"><rect x="1" y="3" width="14" height="10" fill="#d89b2b"/><path d="M1 3l7 6 7-6" fill="none" stroke="#fff" stroke-width="1.3"/></svg>
          info@solvanecrest.com
        </li>
        <li>
          <svg viewBox="0 0 16 16" aria-hidden="true"><g fill="none" stroke="#d89b2b" stroke-width="1.3"><circle cx="8" cy="8" r="6.5"/><ellipse cx="8" cy="8" rx="3" ry="6.5"/><path d="M1.5 8h13M2.5 4.8h11M2.5 11.2h11"/></g></svg>
          solvanecrest.com
        </li>
      </ul>
    </div>
  </section>
</body>
</html>
```